Vellora PhotoStand

Hi There,

I am looking to rebuild my company website.

Here are the development specs for my new site!:

1) I've designed a layout for my site and am looking for someone to incorporate the graphics into a word press template. Enclosed is a screen grab of the look and feel (all of the images / graphic working files are available).

2) The site needs to be built on a wordpress platform so that I can regularly edit the site content and make changes / updates

4) The web content (text) has not been finalized and is still being created. For now, I would really like to get the site developed (from a functionality standpoint) and provide text for each page as we finalize the site development.

I'm really excited to get my site redeveloped and launched!

Industry/Entity Type

It Company

Requirements
Must have
• Home Page to have rotating images

```html
<!DOCTYPE html>
<html lang="en">
<head>
<meta charset="utf-8">
<title>Vellora PhotoStand</title>
<link href="https://fonts.googleapis.com/css2?family=Ubuntu:ital,wght@0,400;0,500;0,700;1,400;1,500;1,700&family=Fjalla+One&family=Cinzel:wght@700&display=swap" rel="stylesheet">
<style>
:root{
  --ink:#222;
  --muted:#444;
  --grey-logo:#5b5b5d;
  --blue:#2f5fc4;
  --blue-bright:#3a6fd8;
  --magenta:#a8245f;
  --magenta-btn:#b3296d;
  --band:#1b1b1b;
  --panel:#2a2a2a;
  --nav:#2b2b2b;
  --nav-line:#0e0e0e;
  --card:#ededed;
  --card-head:#e4e4e4;
  --white:#fff;
}
*{margin:0;padding:0;box-sizing:border-box}
html,body{width:988px;height:1200px;overflow:hidden;background:var(--white)}
body{position:relative;font-family:"Ubuntu",sans-serif;color:var(--ink)}
.abs{position:absolute}

.brand{left:68px;top:30px;display:flex;align-items:center;gap:10px}
.brand-dot{width:42px;height:42px;border-radius:50%;background:var(--blue-bright)}
.brand-name{font-weight:700;font-size:27px;color:var(--grey-logo);letter-spacing:-0.3px}

.main-nav{left:347px;top:105px;width:571px;height:41px;display:flex;background:var(--nav);border:1px solid var(--nav-line)}
.main-nav a{display:flex;align-items:center;justify-content:center;color:var(--white);text-decoration:none;font-weight:500;font-size:13px;border-left:1px solid var(--nav-line);box-shadow:inset 1px 0 0 #444;background:linear-gradient(#353535,#242424)}
.main-nav a:first-child{border-left:none;box-shadow:none}

.hero-band{left:0;top:146px;width:988px;height:312px;background:var(--band)}
.hero-panel{left:64px;top:190px;width:848px;height:327px;background:var(--panel);box-shadow:0 10px 18px rgba(0,0,0,.45)}
.hero-photo{left:81px;top:207px;width:497px;height:280px;background:radial-gradient(circle at 55% 55%,#f2f2ee 0,#c9cdc6 25%,#5f7a3e 50%,#1d3a6a 85%)}
.hero-title{left:596px;top:205px;font-family:"Fjalla One",sans-serif;font-weight:400;font-size:34px;line-height:42px;color:var(--blue-bright);letter-spacing:.3px}
.hero-copy{left:598px;top:256px;width:296px;font-size:12.4px;line-height:20.6px;color:var(--white)}
.know-more{left:598px;top:434px;width:295px;height:53px;background:var(--magenta-btn);display:flex;align-items:center;justify-content:center;gap:14px;color:var(--white);font-family:"Cinzel",serif;font-weight:700;font-size:29px;text-decoration:none}
.slider-dots{left:286px;top:500px;display:flex;gap:7px}
.slider-dots span{width:9px;height:9px;border-radius:50%;background:#bdbdbd}
.slider-dots span.active{background:#d42020}

.welcome-title{left:68px;top:540px;font-style:italic;font-weight:500;font-size:19px;color:var(--ink)}
.welcome-title em{color:var(--blue);font-style:italic}
.welcome-copy{left:68px;top:573px;width:282px;font-size:11.2px;line-height:15.6px;color:var(--ink)}
.perfect-title{left:69px;top:694px;font-style:italic;font-weight:500;font-size:14px;color:var(--magenta)}
.perfect-list{left:69px;top:728px;width:300px;font-style:italic;font-weight:500;font-size:14px;line-height:21px;color:var(--muted)}

.video-frame{left:374px;top:538px;width:540px;height:295px;border:1px solid #bbb;background:var(--white)}
.video-poster{left:380px;top:545px;width:528px;height:282px;background:radial-gradient(ellipse at 45% 55%,#d9d3c8 0,#b4a48c 30%,#6a3a2a 60%,#1a1414 100%)}

.services{left:0;top:850px;width:988px;height:350px;background:linear-gradient(#f7f6f7,#eeedee)}
.services-rule{top:873px;height:1px;background:#bdbdbd}
.services-title{left:0;width:988px;top:865px;text-align:center;font-weight:500;font-size:13.5px;color:var(--muted)}
.service-card{top:902px;width:200px;height:210px;background:var(--card);box-shadow:0 8px 8px -6px rgba(0,0,0,.3)}
.service-card h3{height:43px;display:flex;align-items:center;justify-content:center;font-weight:500;font-size:14.5px;color:var(--ink);background:var(--card-head);border-bottom:1px solid #d8d8d8}
.service-photo{position:absolute;left:12px;top:55px;width:176px;height:80px}
.service-card p{position:absolute;left:12px;top:146px;width:176px;font-size:11px;line-height:14px;color:var(--ink)}
.read-more{position:absolute;left:12px;top:180px;font-size:9.5px;color:var(--blue);text-decoration:none}

.footer-rule{left:140px;top:1152px;width:710px;height:1px;background:#bdbdbd}
.copyright{left:71px;top:1172px;font-size:9px;color:var(--ink)}
.keep-touch{left:670px;top:1169px;font-weight:500;font-size:13px;color:var(--ink)}
.social{left:777px;top:1162px;display:flex;gap:4px}
.social span{width:29px;height:29px;border-radius:50%;background:#e2e2e2;border:1px solid #cfcfcf}
</style>
</head>
<body>

<header>
  <div class="abs brand"><span class="brand-dot"></span><span class="brand-name">Vellora PhotoStand</span></div>
  <nav class="abs main-nav">
    <a style="width:79px">HOME</a>
    <a style="width:94px">SERVICES</a>
    <a style="width:94px">REVIEWS</a>
    <a style="width:131px">ALBUMGALLERY</a>
    <a style="width:76px">BLOG</a>
    <a style="width:97px">CONTACT</a>
  </nav>
</header>

<section class="hero">
  <div class="abs hero-band"></div>
  <div class="abs hero-panel"></div>
  <div class="abs hero-photo" role="img" aria-label="Close-up of a white satin rose with tulle and green ribbon"></div>
  <h1 class="abs hero-title">PLANNING AN EVENT</h1>
  <p class="abs hero-copy">The Vellora PhotoStand experience captures the essence of your party with ‘instant prints’ that create a buzz at your event while providing a memorable keepsake for your guests. The digital images allow you to share and create masterpieces with hish-res digital prints. Our rained photo booh hosts are onsite the entire timne to make sure you have a worry free event.</p>
  <a class="abs know-more">KNOW MORE
    <svg width="22" height="22" viewBox="0 0 22 22"><circle cx="11" cy="11" r="9" fill="none" stroke="#fff" stroke-width="2.5"/><path d="M7 11h7M11 7.5l3.5 3.5-3.5 3.5" fill="none" stroke="#fff" stroke-width="2.2"/></svg>
  </a>
  <div class="abs slider-dots"><span class="active"></span><span></span><span></span><span></span><span></span><span></span></div>
</section>

<section class="welcome">
  <h2 class="abs welcome-title">welcome to <em>VELLORA PHOTOSTAND</em></h2>
  <p class="abs welcome-copy">The Vellora PhotoStand experience captures the essence of your party with ‘instant prints’ that create a buzz at your event while providing a memorable keepsake for your guests. The digital images allow you to share and create masterpieces with hish-res digital prints. Our rained photo booh hosts are onsite the entire timne to make sure you have a worry free event.</p>
  <h3 class="abs perfect-title">We are perfect for:</h3>
  <p class="abs perfect-list">Weddings, Corporate Events, Holiday&nbsp; Parties, Proms, Graduations, Anniversary &amp; Birthday Parties, Bar/bar Mitzvah’s, Trade Shows, Charity Functions</p>
  <div class="abs video-frame"></div>
  <div class="abs video-poster" role="img" aria-label="Video poster showing a vintage camera with a leather strap"></div>
  <svg class="abs" style="left:618px;top:658px" width="54" height="54" viewBox="0 0 54 54"><circle cx="27" cy="27" r="25" fill="rgba(255,255,255,.55)" stroke="#fff" stroke-width="2"/><path d="M21 16l17 11-17 11z" fill="#fff"/></svg>
</section>

<section class="abs services"></section>
<div class="abs services-rule" style="left:70px;width:370px"></div>
<div class="abs services-rule" style="left:568px;width:344px"></div>
<h2 class="abs services-title">OUR SERVICES</h2>

<article class="abs service-card" style="left:70px">
  <h3>UNLIMITED PRINTS</h3>
  <div class="service-photo" role="img" aria-label="Scattered pile of colourful photo prints" style="background:linear-gradient(135deg,#c98a4a,#d94a7a,#5a86b8)"></div>
  <p>All of our Photo Booth Service include....</p>
  <a class="read-more">Read More ····›</a>
</article>
<article class="abs service-card" style="left:284px">
  <h3>FRIENDLY ATTENDANTS</h3>
  <div class="service-photo" role="img" aria-label="Costumed attendant holding a camera" style="background:linear-gradient(135deg,#1f3f5a,#b0322e,#2a2a2a)"></div>
  <p>All of our Photo Booth Service include....</p>
  <a class="read-more">Read More ····›</a>
</article>
<article class="abs service-card" style="left:498px">
  <h3>GUEST BOOK</h3>
  <div class="service-photo" role="img" aria-label="Open spiral guest book with a pen" style="background:linear-gradient(135deg,#f4f4f4,#e2e2e2,#e07aa8)"></div>
  <p>All of our Photo Booth Service include....</p>
  <a class="read-more">Read More ····›</a>
</article>
<article class="abs service-card" style="left:712px">
  <h3>CUSTOMIZED HEADERS</h3>
  <div class="service-photo" role="img" aria-label="Sample custom print header with couple names and date" style="background:#f1f1ef;border:1px solid #ccc"></div>
  <p>All of our Photo Booth Service include....</p>
  <a class="read-more">Read More ····›</a>
</article>

<footer>
  <div class="abs footer-rule"></div>
  <p class="abs copyright">©2012, vellorastand.com, All Rights Reserved &nbsp;|&nbsp; Terms &amp; Conditions</p>
  <p class="abs keep-touch">KEEP IN TOUCH</p>
  <div class="abs social"><span></span><span></span><span></span><span></span></div>
</footer>

</body>
</html>
```